Brill Insurance Agency - Business Cards

Hello, I am needing new trendy business cards for our Insurance Agency now that I have a new Logo. I have attached our new logo with several color options along with a business card design that I like. I am leaning towards burgundy and blue colors. I have attached our current business card. I have also attached a headshot of our company president, Martin Vale, that you can use if you wish. Thank you so much in advance for all the wonderful designs!!!!

Target Market(s)

We want to look very professional to potential customers and we also want to look very professional so insurance companies will want to contract with us to sell their product.

Industry/Entity Type

Insurance

Contact Information for Business Card

Martin Vale
mvale@brillagency.com
Business: 555-213-4087
Fax: 555-213-7751
Cell: 555-390-2618
Toll Free: 888-555-0194
42 W Elm Rd Butler, MO 64730
www.brillagency.net

Font styles to use
Serif
Sans Serif

Colors
0355a3
3277b5
f04a50
ec1f27

Requirements
Nice to have
• I love creativity. The more creative and balanced a business card design the more I will like it. I would like the card to be printed horizontally instead of vertically.
Should not have
• My project should not have the Allied Coverage Network logo. It is no longer used in the industry.

```html
<!DOCTYPE html>
<html lang="en">
<head>
<meta charset="utf-8">
<title>Brill Insurance Agency – Business Cards</title>
<link rel="stylesheet" href="https://fonts.googleapis.com/css2?family=Montserrat:wght@400;500;700&family=Open+Sans:wght@400&display=swap">
<style>
  :root {
    --backdrop: #02152a;
    --burgundy: #541427;
    --charcoal: #4a4a4a;
    --paper: #ffffff;
    --ink-soft: #f2f2f2;
    --rule-grey: #555555;
  }
  html, body {
    margin: 0;
    width: 1200px;
    height: 1200px;
    overflow: hidden;
    background: var(--backdrop);
  }
  .sheet {
    position: relative;
    width: 1200px;
    height: 1200px;
  }
  .card {
    position: absolute;
    top: 162px;
    width: 500px;
    height: 875px;
    border-radius: 40px;
    overflow: hidden;
  }
  .card--front { left: 70px; background: var(--charcoal); }
  .card--back  { left: 630px; background: var(--burgundy); }

  .front__top {
    position: absolute;
    left: 0; top: 0;
    width: 100%;
    height: 300px;
    background: var(--paper);
  }
  .front__disc {
    position: absolute;
    left: 155px; top: 210px;
    width: 190px; height: 190px;
    border-radius: 50%;
    background: var(--paper);
  }
  .front__company {
    position: absolute;
    left: 0; top: 88px;
    width: 100%;
    margin: 0;
    text-align: center;
    font: 700 30px/1.15 "Montserrat", sans-serif;
    letter-spacing: 0.5px;
    color: var(--burgundy);
    text-transform: uppercase;
  }
  .front__company-rule {
    position: absolute;
    left: 90px; top: 178px;
    width: 320px; height: 2px;
    background: var(--rule-grey);
  }
  .front__name {
    position: absolute;
    left: 0; top: 432px;
    width: 100%;
    margin: 0;
    text-align: center;
    font: 700 40px/1 "Montserrat", sans-serif;
    color: var(--paper);
    text-transform: uppercase;
  }
  .contact-list {
    position: absolute;
    left: 120px; top: 540px;
    margin: 0; padding: 0;
    list-style: none;
  }
  .contact-list li {
    display: flex;
    align-items: center;
    height: 41px;
    font: 400 19px/1 "Open Sans", sans-serif;
    color: var(--ink-soft);
  }
  .contact-list svg {
    width: 24px; height: 24px;
    margin-right: 20px;
    flex: none;
  }
  .front__rule {
    position: absolute;
    left: 0; top: 798px;
    width: 100%; height: 6px;
    background: var(--paper);
  }
  .front__address {
    position: absolute;
    left: 0; top: 814px;
    width: 100%; height: 61px;
    margin: 0;
    background: var(--burgundy);
    color: var(--paper);
    font: 400 18px/56px "Montserrat", sans-serif;
    text-align: center;
  }

  .back__mark {
    position: absolute;
    left: 200px; top: 300px;
    width: 100px; height: 100px;
    border: 6px solid var(--paper);
    border-radius: 50%;
    box-sizing: border-box;
  }
  .back__company {
    position: absolute;
    left: 0; top: 440px;
    width: 100%;
    margin: 0;
    text-align: center;
    font: 700 30px/1.15 "Montserrat", sans-serif;
    color: var(--paper);
    text-transform: uppercase;
  }
</style>
</head>
<body>
<main class="sheet">

  <section class="card card--front" aria-label="Business card front">
    <div class="front__top"></div>
    <div class="front__disc"></div>
    <h1 class="front__company">Brill Insurance<br>Agency Inc</h1>
    <div class="front__company-rule"></div>
    <h2 class="front__name">Martin Vale</h2>
    <ul class="contact-list">
      <li>
        <svg viewBox="0 0 24 24" fill="#fff"><path d="M2 5h20v14H2z M2 5l10 8 10-8" stroke="#4a4a4a" stroke-width="1.5"/></svg>
        mvale@brillagency.com
      </li>
      <li>
        <svg viewBox="0 0 24 24" fill="#fff"><path d="M6 2l4 4-2 3c1 3 4 6 7 7l3-2 4 4-3 4C10 22 2 14 2 5z"/></svg>
        555-213-4087,ext.23
      </li>
      <li>
        <svg viewBox="0 0 24 24" fill="none" stroke="#fff" stroke-width="2"><rect x="3" y="8" width="18" height="11" rx="1"/><rect x="7" y="3" width="10" height="6"/><line x1="7" y1="15" x2="17" y2="15"/></svg>
        555-213-7751
      </li>
      <li>
        <svg viewBox="0 0 24 24" fill="#fff"><path d="M12 3l10 9h-3v9h-5v-6h-4v6H5v-9H2z"/></svg>
        555-390-2618
      </li>
      <li>
        <svg viewBox="0 0 24 24" fill="none" stroke="#fff" stroke-width="2"><circle cx="12" cy="12" r="10"/><path d="M9 7l2 2-1 2c1 1 2 2 3 3l2-1 2 2-2 2c-4 0-8-4-8-8z" fill="#fff" stroke="none"/></svg>
        888-555-0194
      </li>
      <li>
        <svg viewBox="0 0 24 24" fill="none" stroke="#fff" stroke-width="2"><circle cx="12" cy="12" r="10"/><ellipse cx="12" cy="12" rx="4" ry="10"/><line x1="2" y1="12" x2="22" y2="12"/></svg>
        www.brillagency.net
      </li>
    </ul>
    <div class="front__rule"></div>
    <p class="front__address">42 W Elm Rd Maple Falls, KS 66999</p>
  </section>

  <section class="card card--back" aria-label="Business card back">
    <div class="back__mark"></div>
    <p class="back__company">Brill Insurance<br>Agency Inc</p>
  </section>

</main>
</body>
</html>
```